Logo for a recruitment consultancy and executive search firm
The Ashcombe Reeve Partnership
Logo for a recruitment consultancy and executive search firm - Consulting
Creative Brief
Professional
Marian Colbeck
Head of Practice
London office: Belgrove Court 42 Belgrove Court Mayfair London W1K 4PL Dublin office: Block C The Larchfield House Oakpark, Kilbarrow Dublin, 9
marian@ashcombe-reeve.example
www.ashcombe-reeve.example
We will need 3 other business cards details are as follows: Name: Tarek Haddadi Title: Head of Practice Address: London office: Belgrove Court 42 Belgrove Court Mayfair London W1K 4PL Dublin office: Block C The Larchfield House Oakpark, Kilbarrow Dublin, 9 Phone: 020 7946 0321 Mobile: 07700900482 Email: tarek@ashcombe-reeve.example Name: Judith Purcell Title: CEO Address: London office: Belgrove Court 42 Belgrove Court Mayfair London W1K 4PL Dublin office: Block C The Larchfield House Oakpark, Kilbarrow Dublin, 9 Phone: 020 7946 0321 Mobile: 07700 900 615 Email: judith@ashcombe-reeve.example Name: Helen Varty Title: Finance Manager Address: London office: Belgrove Court 42 Belgrove Court Mayfair London W1K 4PL Dublin office: Block C The Larchfield House Oakpark, Kilbarrow Dublin, 9 0321 Mobile: 07700 900 738 email: accounts@ashcombe-reeve.example We want the complete stationary set! The more the merrier as far as I am concerned. folders compliment strips headed paper email signature envelopes presentation format position documents folder you name it we want it!
Black with Ashcombe reeve logo

```html
<!DOCTYPE html>
<html lang="en">
<head>
<meta charset="utf-8">
<title>The Ashcombe Reeve Partnership – Stationery Set</title>
<link rel="stylesheet" href="https://fonts.googleapis.com/css2?family=Cormorant+Garamond:wght@500&family=Lato:wght@400;700&display=swap">
<style>
:root{
  --bg-top:#b9b9b9;
  --bg-bottom:#8f8f8f;
  --ink:#111;
  --paper:#f4f4f4;
  --muted:#8a8a8a;
  --line:#cfcfcf;
  --light:#e9e9e9;
}
*{margin:0;padding:0;box-sizing:border-box}
html,body{width:1200px;height:228px;overflow:hidden}
body{background:linear-gradient(var(--bg-top),var(--bg-bottom));font-family:"Lato",sans-serif;position:relative}
.item{position:absolute;box-shadow:0 2px 5px rgba(0,0,0,.35)}
.dark{background:var(--ink);color:var(--light)}
.light{background:var(--paper);color:var(--ink)}
.brand{font-family:"Cormorant Garamond",serif;font-weight:500;letter-spacing:.12em;text-transform:uppercase;display:flex;align-items:center;gap:4px;white-space:nowrap}
.brand .dot{width:6px;height:6px;border-radius:50%;background:currentColor;flex:none}
.tiny{font-size:3px;line-height:1.3;color:var(--muted)}
.header-bar{position:absolute;left:0;top:0;width:150px;height:46px;background:var(--ink);display:flex;align-items:center;justify-content:center}
.header-bar .brand{font-size:9px;color:var(--light)}
.card{width:40px;height:24px;display:flex;align-items:center;justify-content:center}
.card .brand{font-size:3.4px;gap:2px}
.card .brand .dot{width:3px;height:3px}
.card-back{padding:3px;display:block}
.card-back .name{font-size:3.2px;font-weight:700}
.card-large{width:80px;height:46px;display:flex;align-items:flex-end;padding:5px}
.card-large .brand{font-size:5px}
.letter{width:62px;height:88px;padding:0}
.letter .top{height:10px;background:var(--ink);display:flex;align-items:center;justify-content:center}
.letter .top .brand{font-size:3.4px;color:var(--light);gap:2px}
.letter .top .dot{width:3px;height:3px}
.letter .body{padding:6px 6px 0}
.letter .sign{margin-top:10px;font-size:3px;color:var(--ink)}
.letter .foot{position:absolute;bottom:3px;left:0;right:0;text-align:center}
.slip{width:82px;height:30px;display:flex}
.slip .band{width:26px;background:var(--ink);display:flex;align-items:center;justify-content:center}
.slip .band .brand{font-size:2.6px;color:var(--light);letter-spacing:.06em}
.slip .band .dot{display:none}
.slip .text{padding:4px;flex:1}
.envelope{width:96px;height:46px}
.envelope .flap{position:absolute;left:0;top:0;width:100%;height:12px;background:var(--ink)}
.envelope .brand{position:absolute;left:6px;top:16px;font-size:3.6px;gap:2px}
.envelope .brand .dot{width:3px;height:3px}
.envelope .addr-lines{position:absolute;left:44px;top:24px;width:40px}
.envelope .addr-lines span{display:block;height:1px;background:var(--line);margin-bottom:4px}
.dl{width:130px;height:40px}
.dl .band{position:absolute;right:0;top:0;width:34px;height:100%;background:var(--ink);display:flex;align-items:center;justify-content:center}
.dl .band .brand{font-size:3px;color:var(--light);gap:2px}
.dl .band .dot{width:3px;height:3px}
.folder{width:112px;height:180px;display:flex;flex-direction:column;align-items:center;justify-content:center}
.folder .brand{font-size:6.5px}
.folder-inner{width:100px;height:170px;background:#5b5b5b}
.folder-card{width:34px;height:18px;display:flex;align-items:center;justify-content:center}
.folder-card .brand{font-size:2.4px;gap:1.5px}
.folder-card .brand .dot{width:2px;height:2px}
</style>
</head>
<body>

<div class="header-bar item"><span class="brand"><span class="dot"></span>Ashcombe Reeve</span></div>

<!-- business cards -->
<div class="item card dark" style="left:8px;top:55px"><span class="brand"><span class="dot"></span>Ashcombe Reeve</span></div>
<div class="item card light card-back" style="left:52px;top:55px"><div class="name">Marian Colbeck</div><div class="tiny">Head of Practice<br>020 7946 0321<br>marian@ashcombe-reeve.example</div></div>
<div class="item card dark" style="left:90px;top:55px"><span class="brand"><span class="dot"></span>Ashcombe Reeve</span></div>
<div class="item card light card-back" style="left:8px;top:86px"><div class="name">Tarek Haddadi</div><div class="tiny">Head of Practice<br>07700900482<br>tarek@ashcombe-reeve.example</div></div>
<div class="item card dark" style="left:52px;top:86px"><span class="brand"><span class="dot"></span>Ashcombe Reeve</span></div>
<div class="item card light card-back" style="left:90px;top:86px"><div class="name">Judith Purcell</div><div class="tiny">CEO<br>07700 900 615<br>judith@ashcombe-reeve.example</div></div>
<div class="item card light card-back" style="left:8px;top:117px"><div class="name">Helen Varty</div><div class="tiny">Finance Manager<br>07700 900 738<br>accounts@ashcombe-reeve.example</div></div>
<div class="item card dark" style="left:52px;top:117px"><span class="brand"><span class="dot"></span>Ashcombe Reeve</span></div>
<div class="item card-large dark" style="left:8px;top:150px"><span class="brand"><span class="dot"></span>Ashcombe Reeve</span></div>

<!-- letterheads -->
<article class="item letter light" style="left:150px;top:24px">
  <div class="top"><span class="brand"><span class="dot"></span>Ashcombe Reeve</span></div>
  <div class="body tiny">Dear Client,<br>Thank you for your interest in our executive search services. We look forward to working together.
    <div class="sign">Marian Colbeck</div></div>
  <div class="foot tiny">Belgrove Court 42 Belgrove Court Mayfair London W1K 4PL</div>
</article>
<article class="item letter light" style="left:221px;top:24px">
  <div class="top"><span class="brand"><span class="dot"></span>Ashcombe Reeve</span></div>
  <div class="body tiny">Dear Client,<br>Thank you for your interest in our executive search services. We look forward to working together.
    <div class="sign">Marian Colbeck</div></div>
  <div class="foot tiny">Block C The Larchfield House Oakpark, Kilbarrow Dublin, 9</div>
</article>

<!-- compliment slips -->
<div class="item slip light" style="left:298px;top:84px"><div class="band"><span class="brand"><span class="dot"></span>Ashcombe Reeve</span></div><div class="text tiny">With compliments<br>www.ashcombe-reeve.example</div></div>
<div class="item slip light" style="left:298px;top:124px"><div class="band"><span class="brand"><span class="dot"></span>Ashcombe Reeve</span></div><div class="text tiny">With compliments<br>020 7946 0321</div></div>

<!-- envelopes -->
<div class="item envelope light" style="left:392px;top:40px"><div class="flap"></div><span class="brand"><span class="dot"></span>Ashcombe Reeve</span><div class="addr-lines"><span></span><span></span><span></span></div></div>
<div class="item envelope light" style="left:496px;top:40px"><div class="flap"></div><span class="brand"><span class="dot"></span>Ashcombe Reeve</span><div class="addr-lines"><span></span><span></span><span></span></div></div>
<div class="item dl light" style="left:392px;top:128px"><div class="band"><span class="brand"><span class="dot"></span>Ashcombe Reeve</span></div></div>
<div class="item dl light" style="left:530px;top:128px"><div class="band"><span class="brand"><span class="dot"></span>Ashcombe Reeve</span></div></div>
<div class="item envelope light" style="left:610px;top:40px"><div class="flap"></div><span class="brand"><span class="dot"></span>Ashcombe Reeve</span><div class="addr-lines"><span></span><span></span><span></span></div></div>
<div class="item dl light" style="left:676px;top:128px"><div class="band"><span class="brand"><span class="dot"></span>Ashcombe Reeve</span></div></div>
<div class="item envelope dark" style="left:716px;top:40px"><span class="brand" style="color:var(--light)"><span class="dot"></span>Ashcombe Reeve</span></div>

<!-- presentation folder -->
<div class="item folder-inner" style="left:868px;top:28px"></div>
<div class="item folder dark" style="left:950px;top:24px"><span class="brand"><span class="dot"></span>Ashcombe Reeve</span></div>
<div class="item folder-card dark" style="left:1124px;top:150px"><span class="brand"><span class="dot"></span>Ashcombe Reeve</span></div>

</body>
</html>
```